Redesign popular non profit computer donation and recycling website

We wish to make our website more high tech, more modern and feature all of our wonderful stories and offerings in easy to navigate location

Design will need to implement some dynamic variables, such as lists of charities, depot locations, and current content management system, folio grove pro

We wish to feature all of ojr media videos on the front page as well as the most recent donations

we wish to highlight our service offerings, hard drive shredding, volunteer to earn programs, computer store, etc

many of these great things are hard to find on the current layout

There is 2 designs that really catch our attention and we want to improve on both of those

Can we make the bottom blue?

How will the images that are in circles be rotated?

Can we make the latest donations section , 2/3 how it is of the page, and 1/3 make a section for Media, which will include all of our media highlights (vidlorn videos)

We really would like to feature our vidlorn videos on the front page

Can we add a live blurbix feed to the website.

Can we see how you will implement the depot locations inside of this design?
Can we see how you will implement the computer store with this design?
Currently located to www.umk.ca / login / wholesale / computer store shopping cart link

Can we see how you will change the contact us page
Can we see how you plan to display the list of waiting charities
Can we see how you plan to display all of our news feature articles 
Can we see how you plan to display our data destruction page

As we near the end of the contest I'd like to ask the designers the following;

The website must use h1,h2,h3,h4 in hierarchy only.. not starting with h6 or something random.. heading tags must only be used for actual headings.. html5 required, jquery installed and all elements of the design programmed in jquery only.. make sure lists are used in html whenever realistic.. no inline styles.... no classes added to paragraph, heading, or list elements allowed.

Target Market(s)

corporate donors
individuals
charities and non profits
low income people who wish to volunteer and earn a computer or laptop

Industry/Entity Type

Recycling

Requirements
Must have
• current umk logo
• high tech servers, laptops, velto switches, etc
• hard drive shredder in action
• all media stories and videos featured
• all latest donations scrolling
Nice to have
• corporate donors
• individuals
• charities and non profits
• low income people who wish to volunteer and earn a computer or laptop

```html
<!DOCTYPE html>
<html lang="en">
<head>
<meta charset="utf-8">
<title>umk.ca — urban machine keepers</title>
<link href="https://fonts.googleapis.com/css2?family=Questrial&display=swap" rel="stylesheet">
<style>
:root{
  --blue:#2b4f97;
  --green:#8cc63f;
  --green-mid:#5fa62f;
  --ink:#333;
  --footer:#1b1b1b;
  --field:#d9d9d9;
  --white:#fff;
}
*{margin:0;padding:0;box-sizing:border-box}
html,body{width:802px;height:1200px;overflow:hidden;background:var(--white)}
body{font-family:"Questrial",sans-serif;color:var(--ink);position:relative}
ul{list-style:none}
a{color:inherit;text-decoration:none}

/* header */
.site-header{position:absolute;top:0;left:0;width:802px;height:165px}
.brand{position:absolute;left:290px;top:34px;width:180px;text-align:center}
.brand-name{display:block;font-size:22px;color:var(--blue);line-height:26px}
.brand-tagline{display:block;margin-top:24px;font-size:8px;color:var(--blue)}
.login-form{position:absolute;left:611px;top:50px}
.login-field{display:block;width:82px;height:16px;background:var(--field);color:#888;font-size:8px;text-align:center;line-height:16px;margin-bottom:5px}
.login-go{position:absolute;left:82px;top:21px;width:18px;height:16px;background:var(--blue)}
.header-notch{position:absolute;top:97px;left:638px}
.header-rule{position:absolute;top:109px;left:0;width:802px;height:6px;background:var(--blue)}
.main-nav li{position:absolute;top:133px;font-size:14px;color:var(--blue);letter-spacing:.5px;line-height:16px}
.main-nav li:nth-child(1){left:124px}
.main-nav li:nth-child(2){left:210px}
.main-nav li:nth-child(3){left:304px}
.main-nav li:nth-child(4){left:409px}
.main-nav li:nth-child(5){left:516px}
.main-nav li:nth-child(6){left:631px}
.home-icon{position:absolute;left:-22px;top:-1px}

/* hero */
.hero{position:absolute;top:165px;left:0;width:802px;height:318px;
  background:linear-gradient(100deg,#7fbf4b 0%,#3c8a1f 20%,#a8d86a 42%,#4a9a25 62%,#2a7215 78%,#9fd462 100%)}
.hero-visual{position:absolute;left:42px;top:51px;width:524px;height:246px;border-radius:6px;
  background:linear-gradient(160deg,#2a3446 0%,#3a6fb5 45%,#1e2430 100%);opacity:.9}
.side-menu{position:absolute;right:126px;top:32px;text-align:right}
.side-menu li{font-size:13px;color:var(--white);height:25.3px;line-height:23px}
.side-menu .current{background:var(--blue);padding:0 6px;margin-right:-6px;display:inline-block}
.hero-rule{position:absolute;top:483px;left:0;width:802px;height:5px;background:var(--blue)}

/* latest donations */
.donations{position:absolute;top:505px;left:0;width:802px}
.story{position:absolute;top:0;width:242px;height:403px}
.story:nth-child(1){left:30px}
.story:nth-child(2){left:282px}
.story:nth-child(3){left:533px}
.story h2{font-weight:400;font-size:20px;color:var(--blue);text-align:center;height:41px}
.story-photo{width:242px;height:165px}
.photo-boxes{background:linear-gradient(135deg,#b79d74,#6f6357)}
.photo-family{background:linear-gradient(135deg,#8a8a8a,#3b3b3b)}
.photo-event{background:linear-gradient(135deg,#3f4a3a,#7b6b55 60%,#2b3a25)}
.story p{font-size:10.3px;line-height:12.1px;color:var(--ink);margin-top:23px;padding-right:6px}
.read-more{position:absolute;top:375px;right:0;width:90px;height:28px;border-radius:6px;background:var(--blue);color:var(--white);font-size:10px;text-align:center;line-height:28px}

/* monthly archive */
.archive{position:absolute;top:937px;left:0;width:802px;height:214px;background:var(--footer)}
.archive-col{position:absolute;top:34px}
.archive-col:nth-child(1){left:125px}
.archive-col:nth-child(2){left:276px}
.archive-col:nth-child(3){left:428px}
.archive-col:nth-child(4){left:573px}
.archive-col h3{font-weight:400;font-size:20px;line-height:24px;color:var(--green);margin-bottom:20px}
.archive-col li{font-size:11px;color:#e6e6e6;height:23px}

/* footer */
.site-footer{position:absolute;top:1151px;left:0;width:802px;height:49px;
  background:linear-gradient(100deg,#4d9a26 0%,#a5d46b 35%,#4d9a26 65%,#9ed062 100%)}
.footer-brand{position:absolute;left:31px;top:17px;color:var(--white);font-size:11px;line-height:14px}
.footer-brand strong{font-weight:400;margin-right:8px}
.footer-nav li{position:absolute;top:17px;font-size:11px;line-height:14px;color:var(--white)}
.footer-nav li:nth-child(1){left:262px}
.footer-nav li:nth-child(2){left:319px}
.footer-nav li:nth-child(3){left:381px}
.footer-nav li:nth-child(4){left:453px}
.footer-nav li:nth-child(5){left:526px}
.footer-nav li:nth-child(6){left:605px}
.social li{position:absolute;top:19px;font-size:8px;line-height:10px;color:var(--white);display:flex;align-items:center}
.social li::before{content:"";width:9px;height:9px;background:var(--blue);margin-right:3px}
.social li:nth-child(1){left:660px}
.social li:nth-child(2){left:710px}
.social li:nth-child(3){left:754px}
</style>
</head>
<body>

<header class="site-header">
  <div class="brand">
    <span class="brand-name">umk.ca</span>
    <span class="brand-tagline">urban.machine.keepers</span>
  </div>
  <form class="login-form">
    <span class="login-field">USER</span>
    <span class="login-field">PASS</span>
    <span class="login-go"></span>
  </form>
  <svg class="header-notch" width="26" height="13" viewBox="0 0 26 13" aria-hidden="true"><path d="M0 13 L13 0 L26 13Z" fill="var(--blue)"/></svg>
  <div class="header-rule"></div>
  <nav class="main-nav">
    <ul>
      <li><svg class="home-icon" width="16" height="16" viewBox="0 0 16 16" aria-hidden="true"><path d="M2 8 L8 2 L14 8 M4 7 V14 H12 V7" fill="none" stroke="var(--green-mid)" stroke-width="2"/></svg>HOME</li>
      <li>PICKUP</li>
      <li>DONATE</li>
      <li>RECYCLE</li>
      <li>CHARITIES</li>
      <li>LOGIN</li>
    </ul>
  </nav>
</header>

<section class="hero">
  <div class="hero-visual" role="img" aria-label="Two modern laptops, one open at an angle behind the other"></div>
  <ul class="side-menu">
    <li><span class="current">About Us</span></li>
    <li>Drop off items</li>
    <li>Depots</li>
    <li>Jobs</li>
    <li>Volunteer</li>
    <li>Pictures and Videos</li>
    <li>Links</li>
    <li>Memberships</li>
    <li>News</li>
    <li>Contact us</li>
  </ul>
</section>
<div class="hero-rule"></div>

<section class="donations">
  <article class="story">
    <h2>December 2013</h2>
    <div class="story-photo photo-boxes" role="img" aria-label="Staff member celebrating beside boxes of donated computers"></div>
    <p>The UMK makes a donation of laptops and computers to Brightway Special Needs Resource Centre. "These are a much needed upgrade from some of our current computers. Thank you so much UMK for this great donation! We really appreciate it - just look how excited Marla [Dunn] is." Brightway has been providing hope, guidance, and support to families who have children with special needs since 1985.</p>
    <a class="read-more" href="#">READ MORE</a>
  </article>
  <article class="story">
    <h2>November 2013</h2>
    <div class="story-photo photo-family" role="img" aria-label="Mother and son seated with their new laptop"></div>
    <p>UMK grants the wish of a client of Camp Willowmere in BC. Danica and her adorable five-year-old son Oliver are coping with the loss of a loving husband and father, and were in need of a laptop for home use. Camp Willowmere offers bereavement care through counseling, support groups, camps and retreats to individuals and families dealing with loss of loved ones. The organization also holds Grief and Loss Workshops for health care professionals, teachers, and community groups.</p>
    <a class="read-more" href="#">READ MORE</a>
  </article>
  <article class="story">
    <h2>November 2013</h2>
    <div class="story-photo photo-event" role="img" aria-label="Two representatives holding donated laptops beside a holiday tree"></div>
    <p>UMK makes a donation of computers and laptops to Literacy Path Foundation in Calgary. Represented by office administrator Renata Voss, the non-profit organization is dedicated to educating and equipping individuals of all ages facing life-affecting literacy deficiency through free and low-cost training programs and services.</p>
    <a class="read-more" href="#">READ MORE</a>
  </article>
</section>

<section class="archive">
  <div class="archive-col">
    <h3>December</h3>
    <ul><li>link one goes here</li><li>link two goes here</li><li>link one goes here</li><li>link two goes here</li></ul>
  </div>
  <div class="archive-col">
    <h3>November</h3>
    <ul><li>link one goes here</li><li>link one goes here</li><li>link one goes here</li><li>link one goes here</li></ul>
  </div>
  <div class="archive-col">
    <h3>October</h3>
    <ul><li>link one goes here</li><li>link two goes here</li><li>link one goes here</li><li>link two goes here</li></ul>
  </div>
  <div class="archive-col">
    <h3>September</h3>
    <ul><li>link one goes here</li><li>link two goes here</li><li>link one goes here</li><li>link two goes here</li></ul>
  </div>
</section>

<footer class="site-footer">
  <div class="footer-brand"><strong>umk.ca</strong>urban.machine.keepers</div>
  <ul class="footer-nav">
    <li>HOME</li>
    <li>PICKUP</li>
    <li>DONATE</li>
    <li>RECYCLE</li>
    <li>CHARITIES</li>
    <li>LOGIN</li>
  </ul>
  <ul class="social">
    <li>facetrail</li>
    <li>blurbix</li>
    <li>linkrow</li>
  </ul>
</footer>

</body>
</html>
```